Business Card Design For A Renovation Contractor Company

We need a business card for a new company based in Singapore, our company name is "KT Planora". We are a renovation contractor that builds designs into reality. We build more of F&B restaurants, retail stores and commercial offices. We work very closely with designers. The final design should communicate to our client that we are a company that you can trust, that will plan and complete your project without giving you a headache. I like my client to remember my company as "KT". The beauty of SIMPLE is important.

Industry/Entity Type

Contractor

Requirements
Nice to have
• Black or Red base

```html
<!DOCTYPE html>
<html lang="en">
<head>
<meta charset="utf-8">
<title>KT Planora – Business Card Set</title>
<link rel="stylesheet" href="https://fonts.googleapis.com/css2?family=Questrial&family=Source+Sans+3:wght@400;600&display=swap">
<style>
  :root {
    --stage: #3b2b22;
    --brand-red: #ec1c24;
    --ink: #1c1c1c;
    --paper: #ffffff;
    --paper-grid: #f6f7f9;
    --night: #1b2428;
    --label: #f4f1ee;
    --muted: #444444;
  }
  * { box-sizing: border-box; margin: 0; padding: 0; }
  html, body { width: 1200px; height: 913px; overflow: hidden; }
  body {
    position: relative;
    background: var(--stage);
    font-family: "Source Sans 3", sans-serif;
  }
  .card {
    position: absolute;
    overflow: hidden;
    box-shadow: 0 4px 10px rgba(0,0,0,0.45);
  }
  .card--front { left: 90px; top: 146px; width: 464px; height: 266px; background: var(--paper-grid); }
  .card--night { left: 584px; top: 143px; width: 466px; height: 265px; background: var(--night); }
  .card--red   { left: 91px; top: 437px; width: 464px; height: 263px; background: var(--brand-red); }
  .card--white { left: 591px; top: 434px; width: 463px; height: 263px; background: var(--paper); }

  .name-tab {
    position: absolute; left: 0; top: 34px;
    width: 240px; height: 44px;
    background: var(--brand-red);
    border-radius: 0 14px 14px 0;
    color: var(--paper);
    font-size: 20px;
    line-height: 44px;
    padding-left: 29px;
  }
  .name-tab .role { font-size: 12px; }

  .contact {
    position: absolute; left: 30px; top: 182px;
    list-style: none;
    font-size: 11px; color: var(--muted);
    line-height: 15.5px;
  }
  .contact li { display: flex; align-items: center; gap: 6px; }
  .contact svg { width: 9px; height: 9px; fill: var(--brand-red); }

  .brand {
    position: absolute;
    display: flex; flex-direction: column; align-items: center;
    font-family: "Questrial", sans-serif;
  }
  .brand__mark {
    width: 78px; height: 78px; border-radius: 50%;
    border: 6px solid var(--ink);
    margin-bottom: 12px;
  }
  .brand__name {
    font-size: 40px; line-height: 1; letter-spacing: -0.5px;
    color: var(--ink);
    white-space: nowrap;
  }
  .card--front .brand { left: 186px; top: 95px; width: 256px; }
  .card--red .brand { left: 72px; top: 52px; width: 320px; }
  .card--red .brand__mark { width: 82px; height: 82px; border-color: var(--paper); margin-bottom: 14px; }
  .card--red .brand__name { font-size: 48px; color: var(--paper); }
  .card--white .brand { left: 103px; top: 65px; width: 256px; }
  .card--white .brand__mark { width: 68px; height: 68px; margin-bottom: 10px; }
  .card--white .brand__name { font-size: 37px; }

  .web {
    position: absolute; left: 0; right: 0; top: 124px;
    text-align: center;
    color: #e6eaec; font-size: 13px; letter-spacing: 3.5px;
  }

  .label {
    position: absolute;
    color: var(--label);
    font-size: 29px;
  }
  .label--one { left: 944px; top: 90px; }
  .label--two { left: 128px; top: 736px; }
  .label--three { left: 979px; top: 732px; }
</style>
</head>
<body>

  <section class="card card--front" aria-label="Card front">
    <div class="name-tab">Your name, <span class="role">Director</span></div>
    <ul class="contact">
      <li><svg viewBox="0 0 10 10"><path d="M2 0h2l1 3-1.5 1a6 6 0 0 0 2.5 2.5L7 5l3 1v2a2 2 0 0 1-2 2A8 8 0 0 1 0 2a2 2 0 0 1 2-2z"/></svg>012.555.0198</li>
      <li><svg viewBox="0 0 10 10"><path d="M0 2h10v6H0zM0 2l5 3.5L10 2" stroke="#fff" stroke-width="1"/></svg>info@ktplanora.com</li>
      <li><svg viewBox="0 0 10 10"><circle cx="5" cy="5" r="5"/></svg>www.ktplanora.com</li>
    </ul>
    <div class="brand">
      <span class="brand__mark"></span>
      <span class="brand__name">KT Planora</span>
    </div>
  </section>

  <section class="card card--night" aria-label="Card back, dark">
    <p class="web">www.ktplanora.com</p>
  </section>

  <section class="card card--red" aria-label="Card back, red">
    <div class="brand">
      <span class="brand__mark"></span>
      <span class="brand__name">KT Planora</span>
    </div>
  </section>

  <section class="card card--white" aria-label="Card back, white">
    <div class="brand">
      <span class="brand__mark"></span>
      <span class="brand__name">KT Planora</span>
    </div>
  </section>

  <p class="label label--one">Back 1</p>
  <p class="label label--two">Back 2</p>
  <p class="label label--three">Back 3</p>

</body>
</html>
```